Harbor Crest Engineers (HarborCE)
Project: Business cards
Business cards - Information Technology
Business cards
Professional
Dana R. Kessler, CISSP
Principal Systems Engineer
P.O. Box 8073 Huntingtown MD 20639
dkessler@harbor-crest-eng.example
www.harbor-crest-eng.example

```html
<!DOCTYPE html>
<html lang="en">
<head>
<meta charset="utf-8">
<title>Harbor Crest Engineers – Business Cards</title>
<link rel="stylesheet" href="https://fonts.googleapis.com/css2?family=Open+Sans:wght@400;600;700&display=swap">
<style>
  :root {
    --page-bg: #2b2b2d;
    --card-black: #050608;
    --card-white: #fbfbfb;
    --brand-blue: #1f7fd0;
    --blue-deep: #0f5fb0;
    --blue-light: #2f8fe0;
    --brand-orange: #ee7a18;
    --ink-white: #ffffff;
    --ink-soft: #dfe9f5;
    --ink-dark: #2a3440;
  }
  * { margin: 0; padding: 0; box-sizing: border-box; }
  html, body {
    width: 1200px; height: 904px; overflow: hidden;
    background: var(--page-bg);
    font-family: "Open Sans", Arial, sans-serif;
  }
  .canvas { position: relative; width: 1200px; height: 904px; }
  .card {
    position: absolute; width: 620px; height: 354px;
    border-radius: 4px; overflow: hidden;
    box-shadow: 0 18px 40px rgba(0,0,0,.45);
  }
  .card-front { left: 110px; top: 80px; background: var(--card-black); }
  .card-back { left: 470px; top: 470px; background: var(--card-white); }

  .brand { position: absolute; display: flex; flex-direction: column; align-items: center; white-space: nowrap; }
  .brand-row { display: flex; align-items: center; gap: 10px; }
  .brand-dot { border-radius: 50%; background: var(--brand-orange); flex: none; }
  .brand-name { font-weight: 700; color: var(--brand-blue); letter-spacing: .5px; text-transform: uppercase; }
  .brand-tagline { font-weight: 600; text-transform: uppercase; letter-spacing: 1.2px; }

  .card-front .brand { left: 0; right: 0; top: 132px; }
  .card-front .brand-dot { width: 34px; height: 34px; }
  .card-front .brand-name { font-size: 27px; }
  .card-front .brand-tagline { font-size: 9px; color: var(--ink-soft); margin-top: 6px; }

  .back-shapes { position: absolute; inset: 0; }
  .card-back .brand { left: 10px; width: 226px; top: 158px; }
  .card-back .brand-row { gap: 7px; }
  .card-back .brand-dot { width: 16px; height: 16px; }
  .card-back .brand-name { font-size: 13.5px; letter-spacing: .2px; }
  .card-back .brand-tagline { font-size: 6px; letter-spacing: .9px; color: var(--ink-dark); margin-top: 4px; }

  .contact { position: absolute; left: 372px; top: 78px; color: var(--ink-white); }
  .contact-name { font-size: 17px; font-weight: 600; }
  .contact-title { font-size: 11.5px; margin-top: 2px; color: var(--ink-soft); }
  .contact-address { font-size: 11px; margin-top: 16px; line-height: 1.45; }
  .contact-lines { list-style: none; margin-top: 14px; font-size: 11px; }
  .contact-lines li { display: flex; align-items: center; gap: 8px; height: 17px; }
  .contact-lines svg { width: 11px; height: 11px; flex: none; }
</style>
</head>
<body>
<main class="canvas">

  <section class="card card-front" aria-label="Card front">
    <div class="brand">
      <div class="brand-row">
        <span class="brand-dot"></span>
        <span class="brand-name">Harbor Crest Engineers</span>
      </div>
      <span class="brand-tagline">Building Dependable IT Networks</span>
    </div>
  </section>

  <section class="card card-back" aria-label="Card back">
    <svg class="back-shapes" viewBox="0 0 620 354" width="620" height="354" aria-hidden="true">
      <defs>
        <linearGradient id="panelBlue" x1="0" y1="0" x2="1" y2="1">
          <stop offset="0" stop-color="var(--blue-light)"/>
          <stop offset="1" stop-color="var(--blue-deep)"/>
        </linearGradient>
      </defs>
      <path d="M292,0 L332,0 Q262,170 278,354 L236,354 Q222,170 292,0 Z" fill="var(--brand-orange)"/>
      <path d="M332,0 L620,0 L620,354 L278,354 Q262,170 332,0 Z" fill="url(#panelBlue)"/>
    </svg>

    <div class="brand">
      <div class="brand-row">
        <span class="brand-dot"></span>
        <span class="brand-name">Harbor Crest Engineers</span>
      </div>
      <span class="brand-tagline">Building Dependable IT Networks</span>
    </div>

    <div class="contact">
      <p class="contact-name">Dana R. Kessler, CISSP</p>
      <p class="contact-title">Principal Systems Engineer</p>
      <p class="contact-address">P.O. Box 8073<br>Marlowe Bay MD 20711</p>
      <ul class="contact-lines">
        <li><svg viewBox="0 0 12 12"><path d="M2,1 L4.5,1 L5.5,3.5 L4,4.5 Q5,7 7.5,8 L8.5,6.5 L11,7.5 L11,10 Q11,11 10,11 Q1,10.5 1,2 Q1,1 2,1 Z" fill="#fff"/></svg>301-555-0142</li>
        <li><svg viewBox="0 0 12 12"><rect x="3" y="0.5" width="6" height="11" rx="1.2" fill="#fff"/><rect x="4" y="2" width="4" height="6.5" fill="var(--blue-deep)"/></svg>301-555-0187</li>
        <li><svg viewBox="0 0 12 12"><rect x="0.5" y="2" width="11" height="8" rx="1" fill="#fff"/><path d="M1,2.5 L6,6.5 L11,2.5" stroke="var(--blue-deep)" stroke-width="1" fill="none"/></svg>dkessler@harbor-crest-eng.example</li>
        <li><svg viewBox="0 0 12 12"><circle cx="6" cy="6" r="5.2" fill="none" stroke="#fff" stroke-width="1.1"/><ellipse cx="6" cy="6" rx="2.2" ry="5.2" fill="none" stroke="#fff" stroke-width="1"/><line x1="0.8" y1="6" x2="11.2" y2="6" stroke="#fff" stroke-width="1"/></svg>www.harbor-crest-eng.example</li>
      </ul>
    </div>
  </section>

</main>
</body>
</html>
```